Business Card for Modern Marketing Consultancy

Business card needed for marketing consultancy with existing logo.

Lanternway Co is a specialized boutique marketing consultancy that provides startup, small and mid size consumer businesses thought leadership and implementation of marketing strategies to help your business grow.

Our expertise, experience and industry knowledge stems from some of New York’s top global beauty and retail companies and allows us to draw from an array of successful marketing strategies and growth tactics tailored to suit the needs of your business

lanternwayco.example

Target Market(s)

start up, small and mid size consumer packaged goods businesses

Industry/Entity Type

Leadership

Requirements
Must have
• Must have the logo of the business and use of the exact colors of the logo.
Must be simple, sleek, modern and clean. Must make a statement and be eye catching.

Front: looking for unique design or visual statement with logo and tagline

Back of card should have:
logo - if not use on front.
Delia R. Horvath
Founder
Lanternway Co
m: 555.014.2276
deliahorvath@lanternwayco.example
lanternwayco.example

Please use the following words as these describe my services:
strategy analytics branding research

Please refer to the website look and feel: lanternwayco.example

Please kindly note that I am looking for a unique design that I cannot do myself with a template. thank you.
Nice to have
• Please also try and incorporate additional files attached.

```html
<!DOCTYPE html>
<html lang="en">
<head>
<meta charset="utf-8">
<title>Lanternway Co — Business Card</title>
<link rel="stylesheet" href="https://fonts.googleapis.com/css2?family=Poppins:wght@500&family=Krona+One&family=Michroma&family=Arimo:wght@400&display=swap">
<style>
  :root {
    --paper: #ffffff;
    --graphite: #4b4b4b;
    --plum: #8c0d56;
    --magenta: #c8149f;
    --rule: #111111;
  }
  * { margin: 0; padding: 0; box-sizing: border-box; }
  html, body { width: 1080px; height: 1200px; overflow: hidden; background: var(--paper); }
  .sheet { position: relative; width: 1080px; height: 1200px; }

  .card-front { position: absolute; left: 0; top: 0; width: 1080px; height: 600px; }
  .wordmark {
    position: absolute; left: 90px; top: 232px;
    display: flex; align-items: center; gap: 24px;
  }
  .wordmark-name {
    font-family: "Poppins", sans-serif; font-weight: 500;
    font-size: 104px; line-height: 1; letter-spacing: -2px;
    color: var(--graphite);
  }
  .wordmark-dot { width: 64px; height: 64px; border-radius: 50%; background: var(--magenta); }

  .divider { position: absolute; left: 0; top: 589px; width: 1080px; height: 2px; background: var(--rule); }

  .card-back { position: absolute; left: 0; top: 591px; width: 1080px; height: 609px; }
  .person { position: absolute; left: 265px; top: 112px; }
  .person-name {
    font-family: "Krona One", sans-serif; font-size: 41px;
    color: var(--plum); line-height: 1.1;
  }
  .person-role {
    font-family: "Michroma", sans-serif; font-size: 24px;
    color: var(--plum); margin-top: 4px;
  }
  .back-mark {
    position: absolute; left: 106px; top: 352px;
    display: flex; align-items: center; gap: 14px;
  }
  .back-mark-dot { width: 40px; height: 40px; border-radius: 50%; background: var(--magenta); }
  .back-mark-name {
    font-family: "Poppins", sans-serif; font-weight: 500;
    font-size: 34px; color: var(--magenta);
  }
  .contact {
    position: absolute; left: 497px; top: 318px;
    font-family: "Arimo", sans-serif; font-size: 31px; line-height: 40px;
    color: var(--plum); font-style: normal;
  }
</style>
</head>
<body>
<main class="sheet">
  <section class="card-front">
    <div class="wordmark">
      <span class="wordmark-name">Lanternway Co</span>
      <span class="wordmark-dot"></span>
    </div>
  </section>

  <div class="divider"></div>

  <section class="card-back">
    <div class="person">
      <h1 class="person-name">Delia R. Horvath</h1>
      <p class="person-role">Founder</p>
    </div>
    <div class="back-mark">
      <span class="back-mark-dot"></span>
      <span class="back-mark-name">Lanternway Co</span>
    </div>
    <address class="contact">
      <div>Lanternway Co</div>
      <div>m: 555.014.2276</div>
      <div>deliahorvath@lanternwayco.example</div>
      <div>lanternwayco.example</div>
    </address>
  </section>
</main>
</body>
</html>
```